Control panel UI redesign for a learning simulation

Hello. I'm producing a learning simulation and need help with designing a control panel. You will see the panel on the bottom of the image. The look, colors, size, placement, etc. can change, but it has to remain horizontal, that's my only requirement. Overall, I'm open to suggestions. Thank you for your help!

NOTE: the last two items (success rate and progress) are indicators, not buttons, so they should look different from the buttons.

Industry/Entity Type

Learning

Other font styles liked:
• Open Sans

```html
<!DOCTYPE html>
<html lang="en">
<head>
<meta charset="utf-8">
<title>Simulation Control Panel</title>
<link href="https://fonts.googleapis.com/css2?family=Open+Sans:wght@400;600;700&display=swap" rel="stylesheet">
<style>
  :root {
    --wall: #cfcbc4;
    --wall-light: #e4e1dc;
    --ceiling: #f7f7f5;
    --floor: #eeeeec;
    --wood: #9a6d45;
    --bar-bg: rgba(236, 236, 234, 0.92);
    --bar-divider: #d4d4d2;
    --icon: #8e8e8e;
    --label: #6d6d6d;
    --active: #e98a2a;
    --active-dark: #c8691a;
    --active-icon: #f6b13c;
    --indicator-bg: #5e5e5e;
    --indicator-border: #777;
    --nav-bg: #5a5a5a;
    --white: #ffffff;
    --x-blue: #2a8bff;
    --y-green: #3fd43f;
  }
  * { margin: 0; padding: 0; box-sizing: border-box; }
  html, body { width: 1200px; height: 675px; overflow: hidden; font-family: "Open Sans", sans-serif; }
  .stage { position: relative; width: 1200px; height: 675px; overflow: hidden; }
  .scene-backdrop {
    position: absolute; inset: 0;
    background:
      linear-gradient(180deg, var(--ceiling) 0%, var(--ceiling) 7%, var(--wall-light) 8%, var(--wall) 55%, var(--wood) 72%, var(--floor) 88%, var(--floor) 100%);
  }
  .control-bar {
    position: absolute; left: 278px; top: 604px; width: 644px; height: 64px;
    display: flex; background: var(--bar-bg);
  }
  .control {
    width: 78px; height: 64px; display: flex; flex-direction: column;
    align-items: center; justify-content: flex-end; padding-bottom: 4px;
    border-right: 1px solid var(--bar-divider);
  }
  .control svg { width: 36px; height: 36px; margin-bottom: 6px; }
  .control .label { font-size: 8px; letter-spacing: 0.7px; color: var(--label); text-transform: uppercase; font-weight: 600; }
  .control.wide { width: 84px; }
  .control.active { background: linear-gradient(180deg, var(--active) 0%, var(--active-dark) 100%); border-right: none; }
  .control.active .label { color: var(--white); font-weight: 700; }
  .indicator {
    height: 64px; background: var(--indicator-bg); border: 1px solid var(--indicator-border);
    display: flex; flex-direction: column; align-items: center; justify-content: center; color: var(--white);
  }
  .indicator.success { width: 90px; justify-content: flex-end; padding-bottom: 4px; }
  .indicator.success svg { width: 64px; height: 38px; margin-bottom: 3px; }
  .indicator .label { font-size: 8px; letter-spacing: 0.6px; font-weight: 700; text-transform: uppercase; }
  .indicator.progress { width: 78px; font-size: 13px; line-height: 15px; text-align: center; }
  .progress .x { color: var(--x-blue); font-weight: 700; }
  .progress .y { color: var(--y-green); font-weight: 700; }
  .nav { position: absolute; top: 604px; width: 61px; height: 64px; background: var(--nav-bg);
    display: flex; flex-direction: column; align-items: center; justify-content: flex-end; padding-bottom: 4px; color: var(--white); }
  .nav svg { width: 40px; height: 24px; margin-bottom: 12px; }
  .nav .label { font-size: 8px; font-weight: 700; letter-spacing: 0.6px; }
  .nav.prev { left: 1065px; }
  .nav.next { left: 1128px; }
</style>
</head>
<body>
<div class="stage">
  <div class="scene-backdrop" role="img" aria-label="Photo of a modern office with a wooden desk, black chairs, a world map screen on the wall and framed bird prints"></div>

  <nav class="control-bar">
    <div class="control wide">
      <svg viewBox="0 0 36 36" fill="none" stroke="var(--icon)" stroke-width="1.6"><circle cx="18" cy="18" r="15"/><ellipse cx="18" cy="18" rx="7" ry="15"/><line x1="18" y1="3" x2="18" y2="33"/><line x1="3" y1="18" x2="33" y2="18"/><path d="M6 10h24M6 26h24"/></svg>
      <span class="label">Map</span>
    </div>
    <div class="control">
      <svg viewBox="0 0 36 36"><path d="M11 3h14v30l-7-7-7 7z" fill="var(--icon)"/></svg>
      <span class="label">Bookmarks</span>
    </div>
    <div class="control active">
      <svg viewBox="0 0 36 36"><path d="M7 2h15l8 8v24H7z" fill="var(--active-icon)" stroke="var(--active-dark)" stroke-width="1"/><path d="M22 2v8h8" fill="none" stroke="var(--active-dark)" stroke-width="1"/></svg>
      <span class="label">Case Profile</span>
    </div>
    <div class="control">
      <svg viewBox="0 0 36 36" fill="none" stroke="var(--icon)" stroke-width="1.8"><path d="M24 6H5v26h22V16"/><path d="M31 4l-14 14-2 5 5-2 14-14z"/></svg>
      <span class="label">Notes</span>
    </div>
    <div class="control">
      <svg viewBox="0 0 36 36"><rect x="2" y="7" width="32" height="22" fill="var(--icon)"/><path d="M2 7l16 13 16-13M2 29l12-11M34 29l-12-11" fill="none" stroke="var(--bar-bg)" stroke-width="1.6"/></svg>
      <span class="label">Email</span>
    </div>
    <div class="control">
      <svg viewBox="0 0 36 36"><ellipse cx="18" cy="15" rx="16" ry="11" fill="var(--icon)"/><path d="M9 23l-3 9 10-7z" fill="var(--icon)"/></svg>
      <span class="label">Chat</span>
    </div>
    <div class="indicator success">
      <svg viewBox="0 0 64 38" fill="none" stroke-width="7">
        <path d="M6 34 A26 26 0 0 1 11 19" stroke="#e0261b"/>
        <path d="M12 17 A26 26 0 0 1 24 9" stroke="#f06a14"/>
        <path d="M26 8 A26 26 0 0 1 38 8" stroke="#f6c514"/>
        <path d="M40 9 A26 26 0 0 1 52 17" stroke="#a5d12a"/>
        <path d="M53 19 A26 26 0 0 1 58 34" stroke="#2fa83a"/>
        <path d="M32 34 L43 20" stroke="#eeeeee" stroke-width="2.5"/>
        <circle cx="32" cy="34" r="3" fill="#eeeeee" stroke="none"/>
      </svg>
      <span class="label">Success Rate</span>
    </div>
    <div class="indicator progress">
      <span>CALL</span>
      <span><span class="x">X</span> OF <span class="y">Y</span></span>
    </div>
  </nav>

  <div class="nav prev">
    <svg viewBox="0 0 40 24" fill="none" stroke="var(--white)" stroke-width="2"><path d="M38 12H3M13 2L3 12l10 10"/></svg>
    <span class="label">PREV</span>
  </div>
  <div class="nav next">
    <svg viewBox="0 0 40 24" fill="none" stroke="var(--white)" stroke-width="2"><path d="M2 12h35M27 2l10 10-10 10"/></svg>
    <span class="label">NEXT</span>
  </div>
</div>
</body>
</html>
```